Maplerise Trading Inc. needs an innovative idea for letterhead and visiting cards.

Maplerise Trading Inc. is a Canadian brand since 2007. It is a renown dealer of kids and office furniture locally. Moreover, exporting electric fixtures e.g. switches, LED's, down-lights etc. to Middle East and Africa. We have initiated a number of steps including re-branding, to boost our export in 2020. We have successfully designed our new logo a few months ago through 'Artfolio' and now we are looking for an innovative idea for a letterhead.
Some key points:
• Red, black and white are the three colors used in all our packaging and furniture. (grey is optional)
• Shouldn’t be too wide.
• Use of watermark is preferable.
• You can visit our North American site at www.mapleriseinc.com. Export website of the company will be launched soon. www.mapleriseinc.ca
• Same letterhead will be used locally and internationally.
• Our new logo and sample packaging is attached.

```html
<!DOCTYPE html>
<html lang="en">
<head>
<meta charset="utf-8">
<title>Maplerise Trading – Letterhead</title>
<link rel="stylesheet" href="https://fonts.googleapis.com/css2?family=Open+Sans:wght@400;600;700&display=swap">
<style>
  :root {
    --backdrop: #d9d9d9;
    --paper: #ffffff;
    --ink: #231f20;
    --ink-soft: #555555;
    --brand-red: #a41e22;
    --rule: #bdbdbd;
    --signature-tone: #e6e6e6;
  }
  * { margin: 0; padding: 0; box-sizing: border-box; }
  html, body {
    width: 1200px; height: 1200px; overflow: hidden;
    background: var(--backdrop);
    font-family: "Open Sans", Arial, sans-serif;
    color: var(--ink);
  }
  .letterhead {
    position: absolute; left: 193px; top: 29px;
    width: 814px; height: 1142px;
    background: var(--paper);
    box-shadow: 0 4px 18px rgba(0,0,0,.25);
  }
  .spine { position: absolute; left: 0; top: 0; width: 31px; height: 100%; background: var(--ink); }
  .spine-accent { position: absolute; left: 0; top: 1052px; width: 31px; height: 40px; background: var(--brand-red); }

  .brand { position: absolute; left: 106px; top: 96px; display: flex; align-items: center; gap: 10px; }
  .brand-square { width: 20px; height: 20px; background: var(--brand-red); }
  .brand-name { font-weight: 600; font-size: 26px; color: var(--brand-red); letter-spacing: .5px; }

  .recipient { position: absolute; left: 105px; top: 258px; font-size: 13px; line-height: 19px; }
  .salutation { position: absolute; left: 105px; top: 367px; font-size: 13px; }
  .body-copy { position: absolute; left: 105px; top: 404px; width: 608px; font-size: 12.8px; line-height: 25.5px; color: var(--ink); }
  .body-copy p + p { margin-top: 25.5px; }

  .signature-mark { position: absolute; left: 103px; top: 854px; width: 110px; height: 34px; background: var(--signature-tone); border-radius: 4px; }
  .signatory { position: absolute; left: 103px; top: 891px; font-size: 13px; line-height: 15px; }
  .signatory-name { font-weight: 700; }

  .footer-address { position: absolute; left: 107px; top: 1059px; font-size: 9.5px; line-height: 16px; color: var(--ink-soft); }
  .footer-divider { position: absolute; left: 261px; top: 1052px; width: 1px; height: 40px; background: var(--rule); }
  .contact { position: absolute; top: 1064px; display: flex; align-items: center; gap: 6px; font-size: 9.5px; color: var(--ink-soft); }
  .contact svg { width: 11px; height: 11px; fill: var(--brand-red); }
  .contact-phone { left: 280px; }
  .contact-email { left: 397px; }
  .web-band { position: absolute; left: 615px; top: 1052px; width: 167px; height: 40px; background: var(--brand-red);
    display: flex; align-items: center; padding-left: 15px; gap: 6px; color: #fff; font-size: 9.5px; }
  .web-band svg { width: 10px; height: 10px; fill: none; stroke: #fff; stroke-width: 1.4; }
  .web-band-end { position: absolute; left: 782px; top: 1052px; width: 32px; height: 40px; background: var(--ink); }
</style>
</head>
<body>
<main class="letterhead">
  <div class="spine"></div>
  <div class="spine-accent"></div>

  <header class="brand">
    <span class="brand-square"></span>
    <span class="brand-name">Maplerise Trading</span>
  </header>

  <address class="recipient" style="font-style:normal">
    Mr/s<br>First &amp; Last name<br>Company Name<br>Address
  </address>

  <p class="salutation">Dear Sir</p>

  <section class="body-copy">
    <p>This is a sample letter that has been placed to demonstrate typing remat (Your Company). letterhead design. When positioned properly, it will serve to work in harmony with all other elements letterhead. This letterhead design is meant to project an image</p>
    <p>This letterhead design is meant project an image of professionalism reliability. By using simple aligen we have created a very spacious feeling. The simplicity suggest rengththe spaciousnes contributes h aesthetics the layout. These basic qualities along with te (Your Company)</p>
    <p>look and helps reinforce the (Your Company) brand. letterhead design is meant to project an image p design. When positioned properly, it will serve to work in harmony all the other elements letterhead. sionalism and reliability.</p>
    <p>This letterhead design is based on the (Form of your logo) form (Your Company) logo. Each stationery we have created a very spacious feeling. The simplicity suggests strength the spaciousnes contribute part of the (Form of your logo).</p>
  </section>

  <div class="signature-mark" role="img" aria-label="Handwritten signature of Elan Ashby"></div>
  <div class="signatory">
    <div class="signatory-name">Elan Ashby</div>
    <div>Manager</div>
  </div>

  <footer>
    <div class="footer-address">48 Birchmount Rd, Unit 210,<br>Oakridge Vale</div>
    <div class="footer-divider"></div>
    <div class="contact contact-phone">
      <svg viewBox="0 0 24 24"><path d="M6.6 10.8a15.1 15.1 0 0 0 6.6 6.6l2.2-2.2a1 1 0 0 1 1-.25 11.4 11.4 0 0 0 3.6.57 1 1 0 0 1 1 1V20a1 1 0 0 1-1 1A17 17 0 0 1 3 4a1 1 0 0 1 1-1h3.5a1 1 0 0 1 1 1c0 1.25.2 2.45.57 3.57a1 1 0 0 1-.25 1z"/></svg>
      +1 (888) 555-0142
    </div>
    <div class="contact contact-email">
      <svg viewBox="0 0 24 24"><path d="M2 5h20v14H2z M2 5l10 8 10-8" /></svg>
      sales@mapleriseinc.com
    </div>
    <div class="web-band">
      <svg viewBox="0 0 12 12"><circle cx="6" cy="6" r="5"/><path d="M1 6h10M6 1c2 2 2 8 0 10M6 1c-2 2-2 8 0 10"/></svg>
      www.mapleriseinc.com
    </div>
    <div class="web-band-end"></div>
  </footer>
</main>
</body>
</html>
```